Mexican Restaurant needs a new Menu Design

Mexican restaurant LA TORTUGA VERDE is renewing its menu, so we need something new.
Since our inception we have given the task of rescuing ingredients, recipes, and traditional and representatives dishes of the culinary techniques of yesteryear.
We are the only restaurant in Guadalajara that manufactures its own dairy natural as fresh cheese, the cream and our already well-known and traditional jocoqui. In addition, we produce organic ranch egg and are currently in the development of organic vegetables cultivated on the slopes of the old Hill which gives our plants benefit from an exceptional microclimate.
Find more information about the restaurant in www.latortugaverde.com.
The menu needs to have the full list of products with the prices, some phrases that speak of the philosophy of the ranch-style-living, photos.
We need the cover, back cover and interiors.
Updates
Thank you so much for the proposals you have submitted for the menu design. We are looking them carefully.
Thank you very much for taking your time to design a proposal for our menu!!!
Target Market(s)
The target is very wide (28-40 yrs.): Young executives, Young families, Housewives.
Industry/Entity Type
Restaurant
Look and feel
Each slider illustrates characteristics of the customer's brand and the style your logo design should communicate.

```html
<!DOCTYPE html>
<html lang="en">
<head>
<meta charset="utf-8">
<title>La Tortuga Verde — Menu</title>
<link href="https://fonts.googleapis.com/css2?family=Bebas+Neue&family=Crimson+Pro:wght@400;600&display=swap" rel="stylesheet">
<style>
  :root {
    --backdrop: #5f4c3e;
    --cover-red: #d5474b;
    --tab-red: #bf353b;
    --sheet-red: #a92d33;
    --tab-ink: #6b1a1f;
    --cover-ink: #4a3c3c;
    --white: #ffffff;
    --paper: #ffffff;
    --ink: #2f2f2f;
    --ink-soft: #555555;
    --accent: #e0655d;
    --rule: #f2c2bd;
  }
  html, body {
    margin: 0;
    width: 1200px;
    height: 900px;
    overflow: hidden;
    background: var(--backdrop);
  }
  .canvas { position: relative; width: 1200px; height: 900px; }
  .cover-shapes { position: absolute; left: 0; top: 0; }

  .cover-title, .cover-menu, .cover-year, .cover-address {
    position: absolute; left: 131px; width: 397px; text-align: center; margin: 0;
  }
  .cover-title {
    top: 591px; font: 28px/1 "Bebas Neue", sans-serif; color: var(--white); letter-spacing: 1px;
  }
  .cover-menu {
    top: 643px; font: 22px/1 "Bebas Neue", sans-serif; color: var(--cover-ink); letter-spacing: 7px;
  }
  .cover-year {
    top: 754px; font: 13px/1 "Crimson Pro", serif; color: var(--white); letter-spacing: 1px;
  }
  .cover-address {
    top: 773px; font: 10px/1 "Crimson Pro", serif; color: #f6dcdc; letter-spacing: .5px;
  }
  .tab-label {
    position: absolute; font: 17px/1 "Bebas Neue", sans-serif; color: var(--tab-ink);
    letter-spacing: 2px; writing-mode: vertical-rl; margin: 0;
  }
  .tab-mains { left: 534px; top: 310px; }
  .tab-seconds { left: 534px; top: 441px; }

  .menu-page {
    position: absolute; left: 664px; top: 278px; width: 373px; height: 524px;
    background: var(--paper); box-shadow: 2px 3px 6px rgba(0,0,0,.35);
  }
  .menu-page > * { position: absolute; left: 0; right: 0; text-align: center; margin: 0; }
  .brand { top: 30px; font: 13px/1 "Bebas Neue", sans-serif; color: var(--accent); letter-spacing: .5px; }
  .menu-heading { top: 66px; font: 17px/1 "Bebas Neue", sans-serif; color: var(--ink); letter-spacing: 5px; }
  .divider-mark { top: 92px; font: 10px/1 "Crimson Pro", serif; color: var(--accent); letter-spacing: 2px; }
  .rule { left: 18px; right: 18px; height: 0; border-top: 1px solid var(--rule); border-bottom: 1px solid var(--rule); padding-top: 2px; }
  .section-title { font: 15px/1 "Bebas Neue", sans-serif; color: #8a8a8a; letter-spacing: 3px; }
  .dish { line-height: 1; }
  .dish-name { display: block; font: 9px/1 "Bebas Neue", sans-serif; color: var(--ink); letter-spacing: .3px; }
  .dish-desc { display: block; margin-top: 2px; font: 7.5px/1 "Crimson Pro", serif; color: var(--ink-soft); }
  .col-left { left: 20px; right: auto; width: 178px; }
  .col-right { left: auto; right: 20px; width: 178px; }
  .frame { top: 342px; left: 30px; right: 30px; }
</style>
</head>
<body>
<div class="canvas">
  <svg class="cover-shapes" width="1200" height="900" viewBox="0 0 1200 900">
    <rect x="526" y="530" width="21" height="282" fill="var(--sheet-red)"/>
    <path d="M526 400 L532 395 L557 414 L557 520 L545 544 L526 544 Z" fill="var(--tab-red)"/>
    <path d="M526 253 L532 253 L557 275 L557 396 L530 420 L526 420 Z" fill="var(--tab-red)"/>
    <rect x="131" y="250" width="397" height="562" fill="var(--cover-red)"/>
  </svg>
  <p class="tab-label tab-mains">MAINS</p>
  <p class="tab-label tab-seconds">SECONDS</p>

  <h1 class="cover-title">LA TORTUGA VERDE</h1>
  <p class="cover-menu">~ MENU ~</p>
  <p class="cover-year">2013</p>
  <p class="cover-address">Av Los Naranjos # 1184, Col. Jardines del Sol, Zapopan, Jalisco</p>

  <section class="menu-page">
    <p class="brand">LA TORTUGA VERDE</p>
    <h2 class="menu-heading">DINNER MENU</h2>
    <p class="divider-mark">···//···</p>
    <div class="rule" style="top:119px"></div>

    <h3 class="section-title" style="top:128px">STARTERS &amp; SALADS</h3>
    <p class="dish" style="top:158px"><span class="dish-name">COUNTRY STYLE SPREADS WITH SALAD AND GUACAMOLE</span><span class="dish-desc">walnuts, cheese, walnuts, cheese, walnuts, cheese,  w/ walnuts, cheese &amp; walnuts, cheese</span></p>
    <p class="dish" style="top:185px"><span class="dish-name">COUNTRY STYLE SPREADS</span><span class="dish-desc">walnuts, cheese, walnuts, cheese, walnuts, cheese,  w/ walnuts, cheese &amp; walnuts, cheese</span></p>

    <p class="dish col-left" style="top:210px"><span class="dish-name">PICANTE PLATE</span><span class="dish-desc">picante bread, chilli, meat &amp; armadillo</span></p>
    <p class="dish col-right" style="top:210px"><span class="dish-name">PICANTE PLATE</span><span class="dish-desc">picante bread, chilli, meat &amp; armadillo</span></p>
    <p class="dish col-left" style="top:233px"><span class="dish-name">PICANTE PLATE</span><span class="dish-desc">picante bread, chilli, meat &amp; armadillo</span></p>
    <p class="dish col-right" style="top:233px"><span class="dish-name">PICANTE PLATE AND TACO</span><span class="dish-desc">picante bread, chilli, meat &amp; armadillo</span></p>
    <p class="dish col-left" style="top:255px"><span class="dish-name">TACO LOCO</span><span class="dish-desc">picante bread, chilli,</span></p>
    <p class="dish col-right" style="top:255px"><span class="dish-name">PICANTE PLATE</span><span class="dish-desc">picante bread, chilli, meat &amp; armadillo</span></p>
    <p class="dish col-left" style="top:277px"><span class="dish-name">PICANTE PLATE</span><span class="dish-desc">picante bread, chilli, meat &amp; armadillo</span></p>
    <p class="dish col-right" style="top:277px"><span class="dish-name">PICANTE PLATE, FUNGHI E PROSCIUTTO</span><span class="dish-desc">picante bread, chilli, meat &amp; armadillo</span></p>

    <div class="rule" style="top:305px"></div>
    <h3 class="section-title" style="top:317px">MAIN COURSES</h3>

    <svg class="frame" width="313" height="45" viewBox="0 0 313 45">
      <g fill="none" stroke="var(--rule)" stroke-width="1">
        <path d="M2 44 L2 14 L10 14 L10 6 L60 6"/>
        <path d="M6 44 L6 18 L14 18 L14 10 L60 10"/>
        <path d="M311 44 L311 14 L303 14 L303 6 L253 6"/>
        <path d="M307 44 L307 18 L299 18 L299 10 L253 10"/>
      </g>
    </svg>

    <p class="dish" style="top:353px"><span class="dish-name">COUNTRY STYLE SPREADS</span><span class="dish-desc">walnuts, cheese, walnuts, cheese, walnuts, cheese,  w/ walnuts, cheese &amp; walnuts, cheese</span></p>
    <p class="dish" style="top:380px"><span class="dish-name">COUNTRY STYLE SPREADS</span><span class="dish-desc">walnuts, cheese, walnuts, cheese, walnuts, cheese,  w/ walnuts, cheese &amp; walnuts, cheese</span></p>
    <p class="dish" style="top:406px"><span class="dish-name">TRADITIONAL STYLE SOUPS FOR VEGETARIANS</span><span class="dish-desc">walnuts, cheese, walnuts, cheese, walnuts, cheese,  w/ walnuts, cheese &amp; walnuts, cheese</span></p>
    <p class="dish" style="top:433px"><span class="dish-name">COUNTRY SPREADS</span><span class="dish-desc">walnuts, cheese, walnuts, cheese, walnuts, cheese,  w/ walnuts, cheese &amp; walnuts, cheese</span></p>

    <div class="rule" style="top:496px"></div>
  </section>
</div>
</body>
</html>
```